Tobias Grenfell Consulting

I've the wording, and the rough layout. See attached MicroSoft Word File. I need a professional to make my postcard "look pretty".

Consulting

```html
<!DOCTYPE html>
<html lang="en">
<head>
<meta charset="utf-8">
<title>Tobias Grenfell Consulting – Postcard</title>
<link href="https://fonts.googleapis.com/css2?family=Arimo:ital,wght@0,400;0,700;1,400;1,700&family=Archivo+Black&family=Oswald:wght@600&display=swap" rel="stylesheet">
<style>
  :root {
    --ink: #111111;
    --brand-blue: #2f3f9a;
    --tick-red: #d42020;
    --accent-red: #c8202a;
    --link-blue: #3a56c8;
    --paper: #ffffff;
  }
  * { margin: 0; padding: 0; box-sizing: border-box; }
  html, body { width: 1098px; height: 1200px; overflow: hidden; background: var(--paper); }
  body { position: relative; font-family: "Arimo", Arial, sans-serif; color: var(--ink); }
  .abs { position: absolute; white-space: nowrap; }
  .side-label { font-family: "Arimo", Arial, sans-serif; font-weight: 700; font-size: 33px; left: 0; line-height: 1; }
  .headline {
    font-family: "Oswald", "Arial Narrow", sans-serif; font-weight: 600; color: var(--brand-blue);
    font-size: 21px; letter-spacing: 0.2px; left: 215px; line-height: 1;
  }
  .secrets { list-style: none; font-size: 15.6px; line-height: 22.7px; }
  .secrets li { position: relative; padding-left: 24px; }
  .secrets li .tick { position: absolute; left: -2px; top: 1px; width: 24px; height: 20px; }
  .secrets strong { font-family: "Archivo Black", "Arial Black", sans-serif; font-weight: 400; letter-spacing: 0.2px; }
  .pitch { font-size: 11.9px; line-height: 16.2px; font-style: italic; }
  .pitch strong { font-weight: 700; font-style: normal; }
  .brand {
    font-family: "Archivo Black", "Arial Black", sans-serif; color: var(--brand-blue);
    font-size: 30px; line-height: 1; letter-spacing: 0.3px;
    transform: scaleX(0.91); transform-origin: left top;
  }
  .turn-over { font-family: "Archivo Black", "Arial Black", sans-serif; font-size: 16px; line-height: 22px; text-align: center; letter-spacing: 0.4px; }
  .divider { left: 134px; top: 718px; width: 862px; border-top: 2px dashed var(--ink); }
  .fail-box { font-size: 12.1px; line-height: 15.7px; }
  .fail-box .title { font-weight: 700; }
  .fail-box .insiders { color: var(--link-blue); font-weight: 700; }
  .find-out { font-style: italic; font-weight: 700; color: var(--accent-red); font-size: 16px; }
  .site-link { font-family: "Archivo Black", "Arial Black", sans-serif; color: var(--brand-blue); font-size: 19.5px; letter-spacing: 0.3px; line-height: 1; }
  .mailing { font-size: 18.6px; line-height: 24px; }
</style>
</head>
<body>
<svg width="0" height="0" style="position:absolute">
  <defs>
    <symbol id="tick" viewBox="0 0 24 20">
      <path d="M2 11 L5 9 L9 14 C13 8 17 4 23 1 C17 6 13 11 9.5 18 Z" fill="var(--tick-red)"/>
    </symbol>
  </defs>
</svg>

<!-- Side A -->
<div class="abs side-label" style="top:2px">Side A</div>
<div class="abs headline" style="top:61px">Learn Small Business Success Secrets only “insiders” know about:</div>
<ul class="abs secrets" style="left:17px; top:85px">
  <li><svg class="tick"><use href="#tick"/></svg>For those people who almost bought from you but did not, what’s the <strong>real reason</strong> why they didn’t buy from you?(And what<br>to do about it?)</li>
  <li><svg class="tick"><use href="#tick"/></svg>How to turn an ordinary service that the customer can find everywhere, into something that the customer <strong>has to buy<br>from you and only you?</strong></li>
  <li><svg class="tick"><use href="#tick"/></svg>How to turn customer’s “scope creeping”, from a business loss, into a <strong>profit generator?</strong></li>
  <li><svg class="tick"><use href="#tick"/></svg>What sort of person would be <strong>eager</strong> to sell to you at below fair market value?</li>
  <li><svg class="tick"><use href="#tick"/></svg>How to best <strong>utilize</strong> your limited operating capital?</li>
  <li><svg class="tick"><use href="#tick"/></svg>What sort of people would be a <strong>waste of time</strong> for your marketing effort?</li>
  <li><svg class="tick"><use href="#tick"/></svg><strong>Other than money</strong>, how to motivate your employees?</li>
  <li><svg class="tick"><use href="#tick"/></svg>How to prevent your employees from <strong>stealing</strong> your business secrets? Setting up a <strong>competing</strong> business down the street from<br>you? And worse still, <strong>taking</strong> your existing customers too?</li>
  <li><svg class="tick"><use href="#tick"/></svg>How to increase the <strong>perceived</strong> value of your products and services in the mind of your customers?</li>
  <li><svg class="tick"><use href="#tick"/></svg>How to market a commodity as a <strong>highly desired “must have” luxury item?</strong></li>
  <li><svg class="tick"><use href="#tick"/></svg>How do you utilize a potentially bad situation and turn the situation into something positive? productive?<br>and most importantly: <strong>Profitable</strong>???!!!</li>
</ul>
<div class="abs pitch" style="left:5px; top:430px">
  “Insiders” who know the answers to these <u>tricky business problems,</u> <strong>get ahead</strong> in business and life. And the <strong>deeper</strong> their understanding to these tricky business<br>
  problems, the <strong>more successful</strong> they become. They have <strong>very little stress</strong> from their businesses; they work very few hours by building their businesses into "auto<br>
  pilot". They have <strong>more free time to enjoy life</strong>.<br>
  If you don't know how to solve these tricky business problems, you will find yourself struggling with your businesses. You will find yourself working very long hours, and<br>
  you have a lot of stress from running your business. If you are not even aware of the existence of this aspect of running a business, your business will not survive. You<br>
  will become part of the statistic: 80% of businesses fail.<br>
  What specific problems are <u>slowing you down, or keeping you stuck,</u> from <strong>reaching your ultimate goals</strong>? What specific challenges are causing you all the<br>
  <u>Stresses? Headaches? Frustrations?</u><br>
  If your situation continues, how will it <u>negatively impact you</u> from achieving your personal fulfillment? If these problems and challenges could be solved, what are the<br>
  <strong>benefits</strong> to you? <strong>Short term benefits? Long term benefits?</strong>
</div>
<div class="abs pitch" style="left:5px; top:610px">To learn how to overcome these problems and challenges: &nbsp;&nbsp; www.ShopFloorInsiderNotes.com</div>
<div class="abs brand" style="left:289px; top:648px">Tobias Grenfell Consulting</div>
<div class="abs turn-over" style="left:768px; top:643px">Turn to the other side<br>for more info ► ► ►</div>

<!-- Side B -->
<div class="abs side-label" style="top:705px">Side B</div>
<div class="abs divider"></div>
<div class="abs headline" style="top:757px">Learn Small Business Success Secrets only “insiders” know about:</div>
<ul class="abs secrets" style="left:17px; top:779px">
  <li><svg class="tick"><use href="#tick"/></svg>How to make people <strong>want to have</strong> what you have for sale?</li>
  <li><svg class="tick"><use href="#tick"/></svg>How to turn new customers into <strong>repeat customers</strong>?</li>
  <li><svg class="tick"><use href="#tick"/></svg>How to make repeat customers <strong>comeback more often</strong>?</li>
  <li><svg class="tick"><use href="#tick"/></svg>How to <strong>spend less time</strong> with each customer,<br>yet increase your profit on each business transaction?</li>
  <li><svg class="tick"><use href="#tick"/></svg>How to get more <strong>operating capital</strong>?</li>
  <li><svg class="tick"><use href="#tick"/></svg>How to <strong>buy low and sell high?</strong></li>
  <li><svg class="tick"><use href="#tick"/></svg>How to <strong>manage employees and contractors</strong>?</li>
  <li style="margin-top:7px"><svg class="tick"><use href="#tick"/></svg>Which marketing methods are a <strong>total waste of time</strong> and money?</li>
</ul>
<div class="abs fail-box" style="left:511px; top:829px">
  <p class="title">Why do 80% of all businesses fail???</p>
  <p>Because their owners didn’t know what<br><span class="insiders">“business insiders”</span> know. <u>They worked very long<br>hours, they had a lot of stresses and headaches, and in<br>the end, due to their lack of business know-how, their</u><br>businesses failed and they were left with a bunch of debt, a broken heart and<br><u>sometimes a broken family too.</u> Don’t become one of them! Become a real<br>“insider”, run a successful business without stress and enjoy life!</p>
</div>
<div class="abs find-out" style="left:679px; top:958px">To find out more:</div>
<div class="abs site-link" style="left:544px; top:980px">www.ShopFloorInsiderNotes.com</div>
<div class="abs brand" style="left:43px; top:997px">Tobias Grenfell Consulting</div>
<div class="abs turn-over" style="left:555px; top:1009px; font-size:17px">Turn to the other side for more info ► ► ►</div>

<div class="abs mailing" style="left:692px; top:1124px">Alex Sample<br>Alex Sample Corporation<br>Anytown USA</div>
</body>
</html>
```